Ophthalmologist Needs Celebrity Endorsed LASIK Poster Advertisement

Dr. Gerald P. Wexley, MD is an eye physician and surgeon in Kauai, Hawaii. He is the premier ophthalmologist on Kauai and is the only LASIK surgeon. LASIK is a vision correction surgery to help patients reduce or eliminate their dependence on glasses and contact lenses. He has performed hundreds of LASIK procedures and recently did the procedure on one of the actresses from the hit movie "Tide Dancer". She has provided us with content and the rights to produce advertisements using her celebrity endorsement of Dr. Wexley and the LASIK procedure. We need a poster advertisement that will be placed in the lobby of our office building (which receives a lot of foot traffic to other offices). This poster should be eye-catching to passerby, but also convey the LASIK message. Our intent is to generate interest in the procedure (people who wear glasses and contact lenses). The final design should communicate the premier image of our ophthalmology practice and generate interest in LASIK. More information on our practice and LASIK can be found at: www.wexleyeyecare-demo.com.
Updates

Reason: I am still getting back to a few designers on their designs and would like to see the changes before I make a final decision. Thanks for your patience!

Target Market(s)

Men and women ages 25-45 who wear glasses or contact lenses

Industry/Entity Type

Building

Requirements
Must have
• The poster should have our company name (Wexley Eye Care) and logo (attached). It should also use at least one of the attached photos of the celebrity. It should also have the following endorsement verbatum:
"Mahalo Dr. Wexley and staff. I will never take my new eyesight for granted. I love it! Thanks for your care and love." Aloha and God Bless, Marta Ibsen, "Nohea" Da Bad Girl

```html
<!DOCTYPE html>
<html lang="en">
<head>
<meta charset="utf-8">
<title>Wexley Eye Care – LASIK Poster</title>
<link href="https://fonts.googleapis.com/css2?family=Cabin:ital,wght@0,400;0,500;1,400&display=swap" rel="stylesheet">
<style>
  :root {
    --poster-yellow: #f4d016;
    --ink: #111111;
    --headline-white: #ffffff;
    --frame-dark: #141414;
    --frame-mid: #2a2a2a;
    --photo-warm: #c79a6b;
    --photo-sea: #4f8fa6;
  }
  * { margin: 0; padding: 0; box-sizing: border-box; }
  html, body {
    width: 800px;
    height: 1200px;
    overflow: hidden;
    background: var(--poster-yellow);
  }
  .poster {
    position: relative;
    width: 800px;
    height: 1200px;
    background: var(--poster-yellow);
    font-family: "Cabin", "Gill Sans", sans-serif;
    color: var(--ink);
  }
  .eyeglasses {
    position: absolute;
    left: 142px;
    top: 130px;
    width: 512px;
    height: 180px;
    border-radius: 30px 30px 90px 90px;
    background: linear-gradient(180deg, var(--frame-mid) 0%, var(--frame-dark) 100%);
  }
  .headline {
    position: absolute;
    top: 350px;
    left: 0;
    width: 800px;
    text-align: center;
    font-size: 68px;
    font-weight: 400;
    letter-spacing: -1px;
    color: var(--headline-white);
    line-height: 1;
  }
  .cut-line {
    position: absolute;
    top: 458px;
    left: 0;
    width: 800px;
    height: 24px;
  }
  .message {
    position: absolute;
    top: 520px;
    left: 196px;
    font-size: 38px;
    line-height: 56px;
    font-weight: 400;
    letter-spacing: -0.5px;
  }
  .endorsement {
    position: absolute;
    top: 730px;
    left: 120px;
    width: 560px;
    display: flex;
    gap: 28px;
    align-items: center;
  }
  .celebrity-photo {
    flex: 0 0 150px;
    height: 190px;
    background: linear-gradient(180deg, var(--photo-sea) 0%, var(--photo-warm) 100%);
  }
  .testimonial {
    font-size: 19px;
    line-height: 27px;
  }
  .testimonial-quote { font-style: italic; }
  .testimonial-author {
    margin-top: 10px;
    font-weight: 500;
  }
  .brand {
    position: absolute;
    top: 960px;
    left: 0;
    width: 800px;
    display: flex;
    flex-direction: column;
    align-items: center;
  }
  .brand-mark {
    width: 120px;
    height: 120px;
  }
  .brand-name {
    margin-top: 26px;
    font-size: 34px;
    font-weight: 400;
    letter-spacing: -0.5px;
  }
</style>
</head>
<body>
  <main class="poster">
    <div class="eyeglasses" role="img" aria-label="Photo of black handmade eyeglass frames"></div>

    <h1 class="headline">NO MORE</h1>

    <svg class="cut-line" viewBox="0 0 800 24" aria-hidden="true">
      <line x1="0" y1="12" x2="748" y2="12" stroke="var(--ink)" stroke-width="1.6" stroke-dasharray="4 4"/>
      <g fill="none" stroke="var(--ink)" stroke-width="2">
        <line x1="754" y1="12" x2="782" y2="6"/>
        <line x1="754" y1="12" x2="782" y2="18"/>
        <circle cx="788" cy="5" r="5"/>
        <circle cx="788" cy="19" r="5"/>
      </g>
    </svg>

    <p class="message">
      We don’t have to tell you<br>
      about our LASIK surgery.<br>
      You’ll see for your self
    </p>

    <section class="endorsement">
      <div class="celebrity-photo" role="img" aria-label="Photo of actress Marta Ibsen, LASIK patient"></div>
      <blockquote class="testimonial">
        <p class="testimonial-quote">“Mahalo Dr. Wexley and staff. I will never take my new eyesight for granted. I love it! Thanks for your care and love.”</p>
        <p class="testimonial-author">Aloha and God Bless,<br>Marta Ibsen, “Nohea” Da Bad Girl</p>
      </blockquote>
    </section>

    <div class="brand">
      <svg class="brand-mark" viewBox="0 0 120 120" aria-hidden="true">
        <circle cx="60" cy="60" r="55" fill="none" stroke="var(--ink)" stroke-width="6"/>
      </svg>
      <div class="brand-name">Wexley Eye Care</div>
    </div>
  </main>
</body>
</html>
```